Flyer Design Project for lawn care business

I need a flyer designed for my lawn care business, "Ashby's Groundcare Services".  It is a family owned small landscaping company. I was thinking something that I can print  2- 3 per page.
I have  2 different logos I can upload to give an idea.  I have seen some I like that are colorfull with neat graphics but I also like some that are simple and elegant.  I would like something that catches your eye and looks professionaly done.

Target Market(s)
Homeowners in Durham, North Carolina with homes usually valued $200,000 or more.
Industry/Entity Type
Landscaping
Requirements
Must have
- I would like the address of my website listed on it, www.ashbygroundcareservices.com
I would like for it to say somewhere, 50% off first service with seasonal service.
Not sure if I want to list some of the services that I offer or just say full service lawn care.
Nice to have
- I have a logo with a bull pushing a lawn mower.  I live in Durham, NC also known as the Bull City.  I am not in love with the logo so feel free to change it or not use it at all.

```html
<!DOCTYPE html>
<html lang="en">
<head>
<meta charset="utf-8">
<title>Ashby's Groundcare Services – Flyer</title>
<link href="https://fonts.googleapis.com/css2?family=Montserrat:wght@700;800&family=Gabriela&family=Roboto+Condensed:wght@700&display=swap" rel="stylesheet">
<style>
  :root {
    --paper: #ffffff;
    --sky: #a6dbeb;
    --ink: #1c1c1c;
    --orange: #f36c1c;
    --red: #e5141b;
    --white: #ffffff;
    --outline: #2a2a2a;
    --leaf: #6aa82c;
  }
  html, body {
    margin: 0;
    padding: 0;
    width: 1200px;
    height: 900px;
    overflow: hidden;
    background: var(--paper);
  }
  .flyer {
    position: relative;
    width: 1200px;
    height: 900px;
    overflow: hidden;
    background: var(--paper);
  }
  .backdrop {
    position: absolute;
    inset: 0;
  }
  .brand-badge {
    position: absolute;
    left: 80px;
    top: 150px;
    display: flex;
    align-items: center;
    gap: 12px;
    font-family: "Montserrat", sans-serif;
    font-weight: 800;
    font-size: 30px;
    line-height: 1.05;
    color: var(--ink);
  }
  .brand-badge .dot {
    width: 26px;
    height: 26px;
    border-radius: 50%;
    background: var(--red);
    flex: none;
  }
  .headline {
    position: absolute;
    margin: 0;
    font-family: "Montserrat", sans-serif;
    font-weight: 800;
    letter-spacing: 1px;
    line-height: 1.1;
    white-space: nowrap;
    text-shadow:
      -2px -2px 0 var(--outline),
       0   -2px 0 var(--outline),
       2px -2px 0 var(--outline),
       2px  0   0 var(--outline),
       2px  2px 0 var(--outline),
       0    2px 0 var(--outline),
      -2px  2px 0 var(--outline),
      -2px  0   0 var(--outline),
       5px  6px 6px rgba(0,0,0,0.45);
  }
  .headline-name {
    left: 372px;
    top: 145px;
    font-size: 98px;
    color: var(--orange);
  }
  .headline-trade {
    left: 180px;
    top: 277px;
    font-size: 58px;
    color: var(--red);
  }
  .offer {
    position: absolute;
    left: 74px;
    top: 425px;
    margin: 0;
    font-family: "Gabriela", serif;
    font-size: 40px;
    color: var(--ink);
    text-shadow: 2px 3px 3px rgba(0,0,0,0.35);
    white-space: nowrap;
  }
  .tagline {
    position: absolute;
    left: 40px;
    top: 748px;
    margin: 0;
    font-family: "Gabriela", serif;
    font-size: 48px;
    color: var(--white);
    white-space: nowrap;
  }
  .web-address {
    position: absolute;
    left: 40px;
    top: 806px;
    margin: 0;
    font-family: "Roboto Condensed", sans-serif;
    font-weight: 700;
    font-size: 52px;
    letter-spacing: 2.3px;
    color: var(--red);
    white-space: nowrap;
  }
  .corner-mark {
    position: absolute;
    left: 860px;
    top: 720px;
    width: 300px;
    display: flex;
    align-items: center;
    justify-content: center;
    gap: 14px;
    font-family: "Montserrat", sans-serif;
    font-weight: 800;
    font-size: 52px;
    color: var(--white);
  }
  .corner-mark .square {
    width: 34px;
    height: 34px;
    background: var(--leaf);
    flex: none;
  }
</style>
</head>
<body>
<main class="flyer">
  <svg class="backdrop" width="1200" height="900" viewBox="0 0 1200 900" aria-hidden="true">
    <defs>
      <linearGradient id="panelShade" x1="0" y1="0" x2="0" y2="1">
        <stop offset="0" stop-color="#d8d8d8"/>
        <stop offset="0.45" stop-color="#8a8a8a"/>
        <stop offset="0.8" stop-color="#2a2a2a"/>
        <stop offset="1" stop-color="#080808"/>
      </linearGradient>
      <linearGradient id="sweepShade" x1="0" y1="0" x2="1" y2="1">
        <stop offset="0" stop-color="#ffffff" stop-opacity="0.9"/>
        <stop offset="1" stop-color="#ffffff" stop-opacity="0"/>
      </linearGradient>
      <linearGradient id="machineShade" x1="0" y1="0" x2="0" y2="1">
        <stop offset="0" stop-color="#6a6a6a" stop-opacity="0.3"/>
        <stop offset="1" stop-color="#3a3a3a" stop-opacity="0.45"/>
      </linearGradient>
    </defs>
    <rect class="panel" x="17" y="22" width="1166" height="858" fill="url(#panelShade)"/>
    <path class="sweep" d="M380 22 C 560 200, 700 420, 740 880 L 1183 880 L 1183 22 Z" fill="url(#sweepShade)" opacity="0.35"/>
    <path class="sweep" d="M620 22 C 900 120, 1120 200, 1183 240 L 1183 22 Z" fill="#ffffff" opacity="0.55"/>
  </svg>

  <svg class="backdrop" width="1200" height="900" viewBox="0 0 1200 900">
    <rect role="img" aria-label="Faint outline illustration of a push lawn mower" x="640" y="250" width="540" height="630" rx="60" fill="url(#machineShade)"/>
  </svg>

  <svg class="backdrop" width="1200" height="900" viewBox="0 0 1200 900" aria-hidden="true">
    <path class="speech-bubble" fill="var(--sky)"
      d="M160 285 C 240 262, 330 270, 420 272 C 600 276, 820 270, 1028 262
         C 1035 300, 1000 350, 930 395 C 830 460, 720 520, 560 560
         C 430 592, 300 600, 230 640 C 205 660, 205 690, 218 712
         C 150 700, 70 640, 40 560 C 20 500, 18 430, 30 370
         C 45 310, 100 292, 160 285 Z"/>
  </svg>

  <div class="brand-badge"><span class="dot"></span><span>Ashby's<br>Lawn Care</span></div>

  <h1 class="headline headline-name">ASHBY'S</h1>
  <h2 class="headline headline-trade">GROUNDCARE SERVICES</h2>

  <p class="offer">50% off first service with seasonal service.</p>

  <p class="tagline">Full Service Lawn Care.</p>
  <p class="web-address">www.ashbygroundcareservices.com</p>

  <div class="corner-mark"><span class="square"></span><span>Ashby's</span></div>
</main>
</body>
</html>
```